Halvery Metal Recyclers - www.halveryrecyclers.com.au

I've just rebranded my business and thought what better way to continue with this than getting a website.
It is going to be fairly basic for now. I've attached quite a few images, feel free to use whichever you like.
And pages description is also attached in a .doc file.
Updates

Hi, this is my first time having a website. I am open to anything and trust the experience and ideas you can bring forward. I will look at extending the deadline so I can take my time to give feedback as needed! Thank you all.

Target Market(s)

Mining and industrial and commercial sectors

Coding

Coded - Design and coding required

Number of Pages Required

5+ page

Requirements
Must have
• Logo/Phone number at the top of every page. "Scrap Metal Specialists" tag line at the top of every page.
Nice to have
• Top Navigation.

```html
<!DOCTYPE html>
<html lang="en">
<head>
<meta charset="utf-8">
<title>Services – Halvery Metal Recyclers</title>
<link href="https://fonts.googleapis.com/css2?family=Oswald:wght@500;600&family=Poppins:wght@400;500;600&display=swap" rel="stylesheet">
<style>
:root{
  --navy:#1f3b6f;
  --navy-dark:#1a3262;
  --sky:#8fb0e6;
  --ink:#2b2b2b;
  --body:#666;
  --muted:#8a8a8a;
  --line:#d8d8d8;
  --white:#fff;
}
*{margin:0;padding:0;box-sizing:border-box}
html,body{width:1200px;height:4804px;overflow:hidden;background:var(--white)}
body{position:relative;font-family:"Poppins",sans-serif;color:var(--body)}
a{color:inherit;text-decoration:none}
.display{font-family:"Oswald",sans-serif;font-weight:500;text-transform:uppercase;letter-spacing:.5px}

/* header */
.site-header{position:absolute;top:0;left:0;width:1200px;height:120px}
.brand{position:absolute;left:162px;top:22px;font-family:"Oswald",sans-serif;font-weight:600;color:var(--navy);font-size:30px;line-height:36px;text-transform:uppercase}
.tagline{position:absolute;left:450px;top:20px;width:300px;text-align:center;color:var(--navy);font-size:22px;display:flex;align-items:center;justify-content:center;gap:10px}
.tagline::before,.tagline::after{content:"";width:18px;height:2px;background:var(--muted)}
.contact-top{position:absolute;left:804px;top:10px;font-size:13px;color:var(--ink);line-height:30px}
.contact-top div{display:flex;align-items:center;gap:10px}
.contact-top svg{width:14px;height:14px;fill:var(--navy)}
.main-nav{position:absolute;left:452px;top:71px;display:flex;align-items:center;font-size:13px;color:var(--ink)}
.main-nav a{margin-right:50px;line-height:34px}
.main-nav a.active{color:var(--navy);font-weight:600}
.main-nav .nav-cta{margin:0 0 0 10px;background:var(--navy);color:var(--white);padding:0 16px;border:2px solid var(--navy);box-shadow:inset 0 0 0 2px var(--white)}

/* hero */
.hero{position:absolute;top:120px;left:0;width:1200px;height:449px;background:linear-gradient(100deg,#2a2a22 0%,#4d4632 35%,#6a5a3a 60%,#3a3a36 100%)}
.hero-title{position:absolute;left:162px;top:180px;color:var(--white);font-size:68px;line-height:1}
.breadcrumb{position:absolute;left:162px;top:266px;color:var(--white);font-size:15px}
.scroll-down{position:absolute;left:573px;top:547px;width:52px;height:52px;border-radius:50%;background:var(--white);box-shadow:0 3px 10px rgba(0,0,0,.15);display:flex;align-items:center;justify-content:center}

/* intro */
.intro-label{position:absolute;left:162px;top:672px;color:var(--navy);font-size:15px;letter-spacing:1.5px;display:flex;align-items:center;gap:10px;font-family:"Poppins",sans-serif;font-weight:500}
.intro-label::after{content:"";width:30px;height:1px;background:var(--muted)}
.intro-heading{position:absolute;left:162px;top:694px;color:#7a7a7a;font-size:44px;line-height:51px}
.intro-text{position:absolute;left:569px;top:694px;width:469px;font-size:13px;line-height:22.5px;text-align:justify;color:var(--body)}
.intro-text strong{color:var(--ink);font-weight:600}

/* services */
.service{position:absolute;left:162px;width:876px;height:290px}
.service-card{position:absolute;top:0;width:389px;height:290px;background:var(--white);box-shadow:0 2px 10px rgba(0,0,0,.12);padding:8px}
.service-card .photo{width:100%;height:100%}
.service.img-left .service-card{left:0}
.service.img-right .service-card{right:0}
.service-body{position:absolute;top:50%;transform:translateY(-50%);width:437px}
.service.img-left .service-body{left:439px}
.service.img-right .service-body{left:0}
.service-title{color:var(--ink);font-size:19px;line-height:24px;margin-bottom:14px}
.service-body p{font-size:13px;line-height:22.7px;text-align:justify;color:var(--body)}
.service-body p+p{margin-top:12px;text-align:left}

/* footer */
.footer-wave{position:absolute;left:0;top:4320px;width:1200px;height:484px}
.footer-col{position:absolute;top:4496px;color:var(--white)}
.footer-col h3{font-size:19px;padding-bottom:10px;border-bottom:1px solid rgba(255,255,255,.3);display:inline-block}
.quick-links{left:162px}
.quick-links ul{list-style:none;margin-top:12px;font-size:13px;line-height:27px}
.quick-links li::before{content:"»";margin-right:10px}
.quick-links li.active{font-weight:600}
.contact-details{left:401px}
.contact-details div{display:flex;align-items:center;gap:12px;font-size:13px;margin-top:26px}
.contact-details div+div{margin-top:18px}
.contact-details svg{width:14px;height:14px;fill:var(--white)}
.footer-brand{position:absolute;left:763px;top:4538px;width:275px;text-align:center;font-family:"Oswald",sans-serif;font-weight:600;color:var(--white);font-size:46px;line-height:50px;text-transform:uppercase}
.footer-rule{position:absolute;left:0;top:4742px;width:1200px;height:1px;background:rgba(255,255,255,.25)}
.copyright{position:absolute;left:0;top:4768px;width:1200px;text-align:center;font-size:12px;color:var(--white)}
</style>
</head>
<body>

<header class="site-header">
  <div class="brand">Halvery<br>Metal Recyclers</div>
  <div class="tagline display">Scrap Metal Specialists</div>
  <div class="contact-top">
    <div><svg viewBox="0 0 24 24"><path d="M6.6 10.8a15.1 15.1 0 0 0 6.6 6.6l2.2-2.2c.3-.3.7-.4 1-.2 1.1.4 2.3.6 3.6.6.6 0 1 .4 1 1V20c0 .6-.4 1-1 1A17 17 0 0 1 3 4c0-.6.4-1 1-1h3.5c.6 0 1 .4 1 1 0 1.3.2 2.5.6 3.6.1.3 0 .7-.2 1z"/></svg>0400 555 018</div>
    <div><svg viewBox="0 0 24 24"><path d="M2 5h20v14H2z M2 5l10 8 10-8" stroke="#fff" stroke-width="1.5"/></svg>info@halveryrecyclers.com.au</div>
  </div>
  <nav class="main-nav">
    <a href="#">Home</a><a href="#">About Us</a><a href="#" class="active">Services</a><a href="#">Online Store</a><a href="#">Blog</a><a href="#" class="nav-cta">Contact Us</a>
  </nav>
</header>

<section class="hero" role="img" aria-label="Scrap metal processing plant with conveyor and heavy drum at night">
  <h1 class="hero-title display">Services</h1>
  <div class="breadcrumb">Home &nbsp;»&nbsp; Services</div>
</section>
<div class="scroll-down"><svg width="20" height="20" viewBox="0 0 24 24" fill="none" stroke="#1f3b6f" stroke-width="2"><path d="M12 4v15M6 13l6 6 6-6"/></svg></div>

<div class="intro-label">SERVICES</div>
<h2 class="intro-heading display">Oxy Cutting and<br>Breaking Down Of</h2>
<p class="intro-text"><strong>Halvery Metal Recyclers</strong> sitmli amet, consectetuer adipiscing elit, sed diam nonummy nibhml euismod tincidunt ut laoreet dolore magna aliquam erat mor volutpat. Ut wisi enim ad minim veniam, quis nostrud exercim tation suscipit lobor commodo consequat.</p>

<main>
  <article class="service img-left" style="top:827px">
    <div class="service-card"><div class="photo" role="img" aria-label="Yellow wheel loader moving rubble" style="background:linear-gradient(180deg,#8aa3c4 0%,#b69062 55%,#a35a36 100%)"></div></div>
    <div class="service-body"><h3 class="service-title display">Large Mining Machinery</h3><p>Lorem ipsum dolor sit amet, consectetuer adipiscing elit, sed diam nonummy nibh euismod tincidunt ut laoreet dolore magna aliquam erat volutpat. Ut wisi enim ad minim veniam, quis nostrud exerci tation ullamcorper suscipit lobortis nisl ut aliquip ex ea commodo consequat. Duis autem vel eum iriure dolor in hendrerit</p></div>
  </article>

  <article class="service img-right" style="top:1139px">
    <div class="service-card"><div class="photo" role="img" aria-label="Excavator with grapple sorting a scrap pile" style="background:linear-gradient(180deg,#a9c3dc 0%,#8d8a82 55%,#6b5f53 100%)"></div></div>
    <div class="service-body"><h3 class="service-title display">Scrap Metal Clean Up and Removal</h3><p>Lorem ipsum dolor sit amet, consectetuer adipiscing elit, sed diam nonummy nibh euismod tincidunt ut laoreet dolore magna aliquam erat volutpat. Ut wisi enim ad minim veniam, quis nostrud exerci tation ullamcorper suscipit lobortis nisl ut aliquip ex ea commodo consequat. Duis autem vel eum iriure dolor in hendrerit</p><p>It is a long established fact that a reader will be distracted by the readable content of a page when looking at its layout. The point of using Lorem Ipsum.</p></div>
  </article>

  <article class="service img-left" style="top:1451px">
    <div class="service-card"><div class="photo" role="img" aria-label="Compact excavator clearing trees on a site" style="background:linear-gradient(180deg,#c7ccc8 0%,#6f7a55 55%,#4e5a34 100%)"></div></div>
    <div class="service-body"><h3 class="service-title display">Minesite Clean Ups and Demolition</h3><p>Lorem ipsum dolor sit amet, consectetuer adipiscing elit, sed diam nonummy nibh euismod tincidunt ut laoreet dolore magna aliquam erat volutpat. Ut wisi enim ad minim veniam, quis nostrud exerci tation ullamcorper suscipit lobortis nisl ut aliquip ex ea commodo consequat. Duis autem vel eum iriure dolor in hendrerit</p></div>
  </article>

  <article class="service img-right" style="top:1763px">
    <div class="service-card"><div class="photo" role="img" aria-label="Worker in hard hat cutting steel outdoors" style="background:linear-gradient(180deg,#7d8a6a 0%,#4b5360 55%,#2c2f36 100%)"></div></div>
    <div class="service-body"><h3 class="service-title display">Subsea – Jetty's, Barges, Pylons, Boats, Anchors, Chain</h3><p>Lorem ipsum dolor sit amet, consectetuer adipiscing elit, sed diam nonummy nibh euismod tincidunt ut laoreet dolore magna aliquam erat volutpat. Ut wisi enim ad minim veniam, quis nostrud exerci tation ullamcorper suscipit lobortis nisl ut aliquip ex ea commodo consequat. Duis autem vel eum iriure dolor in hendrerit</p></div>
  </article>

  <article class="service img-left" style="top:2075px">
    <div class="service-card"><div class="photo" role="img" aria-label="Steel conveyor structure at a minesite under blue sky" style="background:linear-gradient(160deg,#7a6850 0%,#a8a08e 45%,#6ea0d6 100%)"></div></div>
    <div class="service-body"><h3 class="service-title display">Large Minesite Infrastructure</h3><p>Lorem ipsum dolor sit amet, consectetuer adipiscing elit, sed diam nonummy nibh euismod tincidunt ut laoreet dolore magna aliquam erat volutpat. Ut wisi enim ad minim veniam, quis nostrud exerci tation ullamcorper suscipit lobortis nisl ut aliquip ex ea commodo consequat. Duis autem vel eum iriure dolor in hendrerit</p><p>It is a long established fact that a reader will be distracted by the readable content of a page when looking at its layout. The point of using Lorem Ipsum.</p></div>
  </article>

  <article class="service img-right" style="top:2387px">
    <div class="service-card"><div class="photo" role="img" aria-label="Elevated work platform beside a glass building facade" style="background:linear-gradient(90deg,#e2ddd5 0%,#cfc8bd 30%,#2a4aa0 60%,#1e2f7a 100%)"></div></div>
    <div class="service-body"><h3 class="service-title display">EWP and High Risk Work</h3><p>Lorem ipsum dolor sit amet, consectetuer adipiscing elit, sed diam nonummy nibh euismod tincidunt ut laoreet dolore magna aliquam erat volutpat. Ut wisi enim ad minim veniam, quis nostrud exerci tation ullamcorper suscipit lobortis nisl ut aliquip ex ea commodo consequat. Duis autem vel eum iriure dolor in hendrerit</p></div>
  </article>

  <article class="service img-left" style="top:2699px">
    <div class="service-card"><div class="photo" role="img" aria-label="Welder cutting metal with bright sparks" style="background:linear-gradient(135deg,#2a3a5a 0%,#4f6fa8 40%,#8a5a2e 75%,#2a2320 100%)"></div></div>
    <div class="service-body"><h3 class="service-title display">Oxy Cutting and Breaking Down Of</h3><p>Lorem ipsum dolor sit amet, consectetuer adipiscing elit, sed diam nonummy nibh euismod tincidunt ut laoreet dolore magna aliquam erat volutpat. Ut wisi enim ad minim veniam, quis nostrud exerci tation ullamcorper suscipit lobortis nisl ut aliquip ex ea commodo consequat. Duis autem vel eum iriure dolor in hendrerit</p></div>
  </article>

  <article class="service img-right" style="top:3011px">
    <div class="service-card"><div class="photo" role="img" aria-label="Industrial production hall with heavy machinery" style="background:linear-gradient(180deg,#b7c0c8 0%,#7f8a94 50%,#c9cdd0 100%)"></div></div>
    <div class="service-body"><h3 class="service-title display">Heavy Industrial Equipment</h3><p>Lorem ipsum dolor sit amet, consectetuer adipiscing elit, sed diam nonummy nibh euismod tincidunt ut laoreet dolore magna aliquam erat volutpat. Ut wisi enim ad minim veniam, quis nostrud exerci tation ullamcorper suscipit lobortis nisl ut aliquip ex ea commodo consequat. Duis autem vel eum iriure dolor in hendrerit</p></div>
  </article>

  <article class="service img-left" style="top:3323px">
    <div class="service-card"><div class="photo" role="img" aria-label="Close view of a rail track on gravel" style="background:linear-gradient(160deg,#7a5a42 0%,#a98a72 45%,#4a3a30 100%)"></div></div>
    <div class="service-body"><h3 class="service-title display">Rail</h3><p>Lorem ipsum dolor sit amet, consectetuer adipiscing elit, sed diam nonummy nibh euismod tincidunt ut laoreet dolore magna aliquam erat volutpat. Ut wisi enim ad minim veniam, quis nostrud exerci tation ullamcorper suscipit lobortis nisl ut aliquip ex ea commodo consequat. Duis autem vel eum iriure dolor in hendrerit</p></div>
  </article>

  <article class="service img-right" style="top:3635px">
    <div class="service-card"><div class="photo" role="img" aria-label="Robotic arm handling stock in a warehouse" style="background:linear-gradient(180deg,#9aa7b8 0%,#5a6680 50%,#c8a040 100%)"></div></div>
    <div class="service-body"><h3 class="service-title display">Transport and Collection</h3><p>Lorem ipsum dolor sit amet, consectetuer adipiscing elit, sed diam nonummy nibh euismod tincidunt ut laoreet dolore magna aliquam erat volutpat. Ut wisi enim ad minim veniam, quis nostrud exerci tation ullamcorper suscipit lobortis nisl ut aliquip ex ea commodo consequat. Duis autem vel eum iriure dolor in hendrerit</p><p style="text-align:justify">Contrary to popular belief, Lorem Ipsum is not simply random text. It has roots in a piece of classical Latin literature from 45 BC, making it over 2000 years old. Edwin Marlowe, a Latin professor at Ashbury College in Virginia, looked up one of the more obscure Latin words.</p></div>
  </article>

  <article class="service img-left" style="top:3947px">
    <div class="service-card"><div class="photo" role="img" aria-label="Heap of mixed scrap metal parts" style="background:linear-gradient(160deg,#6a4a35 0%,#9a7a5e 50%,#3e2e24 100%)"></div></div>
    <div class="service-body"><h3 class="service-title display">Buyer of All Types of Scrap Metal</h3><p>Lorem ipsum dolor sit amet, consectetuer adipiscing elit, sed diam nonummy nibh euismod tincidunt ut laoreet dolore magna aliquam erat volutpat. Ut wisi enim ad minim veniam, quis nostrud exerci tation ullamcorper suscipit lobortis nisl ut aliquip ex ea commodo consequat. Duis autem vel eum iriure dolor in hendrerit</p></div>
  </article>
</main>

<footer>
  <svg class="footer-wave" viewBox="0 0 1200 484" preserveAspectRatio="none" aria-hidden="true">
    <path d="M0 120 L262 10 L1200 120 L1200 484 L0 484 Z" fill="var(--sky)"/>
    <path d="M0 104 L262 46 L1200 160 L1200 484 L0 484 Z" fill="var(--navy)"/>
  </svg>
  <div class="footer-col quick-links">
    <h3 class="display">Quick Links</h3>
    <ul><li>Home</li><li>About Us</li><li class="active">Services</li><li>Online Store</li><li>Blog</li><li>Contact Us</li></ul>
  </div>
  <div class="footer-col contact-details">
    <h3 class="display">Contact Details</h3>
    <div><svg viewBox="0 0 24 24"><path d="M6.6 10.8a15.1 15.1 0 0 0 6.6 6.6l2.2-2.2c.3-.3.7-.4 1-.2 1.1.4 2.3.6 3.6.6.6 0 1 .4 1 1V20c0 .6-.4 1-1 1A17 17 0 0 1 3 4c0-.6.4-1 1-1h3.5c.6 0 1 .4 1 1 0 1.3.2 2.5.6 3.6.1.3 0 .7-.2 1z"/></svg>0400 555 018</div>
    <div><svg viewBox="0 0 24 24"><path d="M2 5h20v14H2z M2 5l10 8 10-8" stroke="#1f3b6f" stroke-width="1.5"/></svg>info@halveryrecyclers.com.au</div>
  </div>
  <div class="footer-brand">Halvery<br>Metal Recyclers</div>
  <div class="footer-rule"></div>
  <div class="copyright">© 2022 HALVERY METAL RECYCLERS. All Rights Reserved.</div>
</footer>

</body>
</html>
```